Creation of brand identity and website "Folio K"

I am currently seeking an brand, identity and web design for a new project called Folio K. This is a brand new concept from scratch and you have free-reign on the whole design process, taking into account my preference below.

Must include the name "Folio K", or "Folio K: A tale of my Turnaround". Kudos is this forms part of the brands logo

Design that can be easily scaled to potentially include: a blog, timeline and vlogs.

Minimal but effective use of colour (however any colours and combinations permitted

Use of icons/graphics over text wherever possible

Minimal use of frames and borders

I appreciate this is a fairly wide scope so please contact me on tindervale@postmarrow.net with any questions or more information on what the project is.

Target Market(s)

Male and Female 20-40
Blog readers
Selfhelp

Industry/Entity Type

Seeking

Number of Pages Required

1 page

Font styles to use
Serif
Sans Serif

Requirements
Must have
• It is in effect a blog design, so about me section, recent blog / archived posts, reader comments / Q and A section.
• A coded design would be appreciated to make my life easier however I have left the design as uncoded as getting the right design matters more to me and I want to keep the project open to as many designers as possible
Nice to have
• See project description for other details and please ask if you need anything else :)
Should not have
• Mustn't be cluttered or feel fussy
• Promote icons over text
• Frames / multiple borders

```html
<!DOCTYPE html>
<html lang="en">
<head>
<meta charset="utf-8">
<title>Folio K: A tale of my Turnaround</title>
<link href="https://fonts.googleapis.com/css2?family=Montserrat:wght@400;600;700&family=Lato:wght@400;700&display=swap" rel="stylesheet">
<style>
:root{
  --orange:#fd9800;
  --dark:#333333;
  --footer:#2c2c2c;
  --page:#f5f5f5;
  --white:#ffffff;
  --ink:#222222;
  --text:#444444;
  --line:#e3e3e3;
  --tab:#e6e6e6;
  --navy:#2c3e55;
  --net-blue:#1f5fa8;
  --net-red:#d6453d;
  --net-sky:#2ba3dc;
  --net-crimson:#c4302b;
  --net-deep:#0e5c91;
}
*{box-sizing:border-box;margin:0;padding:0}
a{text-decoration:none}
html,body{width:1200px;height:2381px;overflow:hidden}
body{font-family:"Lato",Arial,sans-serif;color:var(--text);background:var(--page);position:relative}
.abs{position:absolute}

/* header */
.site-header{left:0;top:0;width:1200px;height:75px;background:var(--dark);box-shadow:0 2px 4px rgba(0,0,0,.4);z-index:2}
.brand{left:84px;top:18px;font-family:"Montserrat",sans-serif;font-weight:700;font-size:27px;color:var(--white)}
.nav{left:449px;top:0;height:75px;display:flex}
.nav a{display:block;height:75px;line-height:78px;padding:0 16px;color:var(--white);font-family:"Montserrat",sans-serif;font-weight:600;font-size:15px;white-space:nowrap}
.nav a.active{background:var(--orange);padding:0 17px}
.social-top{left:992px;top:31px;display:flex;gap:12px;font-family:"Montserrat",sans-serif;font-weight:600;font-size:11px;color:var(--white);white-space:nowrap}

/* hero */
.hero{left:0;top:75px;width:1200px;height:436px;background:linear-gradient(180deg,#59677c 0%,#8f8d90 35%,#e4a44d 62%,#f5a21f 72%,#5a3a1f 100%)}
.hero-text{left:83px;top:262px;width:420px;font-family:"Montserrat",sans-serif;font-weight:700;font-size:24px;line-height:32px;color:var(--white)}
.hero-dashes{left:83px;top:379px;display:flex;gap:6px}
.hero-dashes span{display:block;width:14px;height:3px;background:var(--white)}

/* cards */
.card{background:var(--white);border:1px solid var(--line)}
.meta{display:flex;align-items:center;font-size:12px;color:var(--ink);white-space:nowrap}
.meta svg{width:13px;height:13px;margin-right:5px;fill:var(--orange)}
.meta .gap{margin-left:26px}
.featured{left:84px;top:556px;width:711px;height:460px}
.featured-photo{left:0;top:0;width:709px;height:265px;background:linear-gradient(180deg,#f1c869 0%,#f7b02c 60%,#e8901a 100%)}
.featured-meta{left:14px;top:290px}
.featured-meta .date{font-size:13.5px;letter-spacing:.3px}
.featured-meta b{font-weight:700;font-size:14px;margin-left:5px}
.featured-title{left:14px;top:320px;font-family:"Montserrat",sans-serif;font-weight:700;font-size:20px;color:var(--ink)}
.featured-text{left:14px;top:354px;width:560px;font-size:15px;line-height:21px;color:var(--ink)}
.btn{display:block;background:var(--orange);color:var(--white);font-family:"Montserrat",sans-serif;font-weight:700;font-size:13px;text-align:center;letter-spacing:.5px}
.featured-btn{left:13px;top:409px;width:121px;height:33px;line-height:33px}

.rule{left:84px;width:711px;height:1px;background:var(--line)}
.post{width:349px;height:199px}
.post-title{left:13px;top:18px;font-family:"Montserrat",sans-serif;font-weight:700;font-size:16px;color:var(--ink);white-space:nowrap}
.post-meta{left:13px;top:55px;font-size:12px}
.post-meta .gap{margin-left:24px}
.post-thumb{left:15px;top:91px;width:81px;height:80px}
.post-text{left:111px;top:91px;width:228px;font-size:12.5px;line-height:17.5px;color:var(--ink)}
.post-text a{color:var(--orange)}

/* sidebar */
.widget{background:var(--white);border:1px solid var(--line)}
.widget-title{font-family:"Montserrat",sans-serif;font-weight:700;font-size:14.5px;color:var(--ink);white-space:nowrap}
.newsletter{left:836px;top:557px;width:280px;height:137px}
.newsletter .widget-title{left:14px;top:12px}
.email{left:13px;top:42px;width:252px;height:35px;border:1px solid #d8d8d8;font-size:11.5px;color:#999;line-height:33px;padding-left:9px}
.subscribe{left:13px;top:91px;width:92px;height:34px;line-height:34px;font-size:11.5px}

.tabs{left:836px;top:727px;width:280px;height:302px}
.tab-bar{left:0;top:0;width:278px;height:34px;background:var(--tab);display:flex}
.tab-bar span{flex:none;white-space:nowrap;font-family:"Montserrat",sans-serif;font-weight:600;font-size:11px;color:var(--ink);line-height:34px;padding:0 9px}
.tab-bar span.on{background:var(--orange);color:var(--white);position:relative}
.tab-bar span.on:after{content:"";position:absolute;left:36px;bottom:-7px;border:7px solid transparent;border-bottom:0;border-top-color:var(--orange)}
.tab-bar span.last{margin-left:auto}
.tab-item{left:12px;width:256px;height:74px}
.tab-thumb{left:0;top:0;width:74px;height:74px;border:1px solid var(--line)}
.tab-text{left:92px;top:6px;width:162px;font-size:12px;line-height:17px;color:var(--ink)}
.view-all{left:200px;top:274px;font-family:"Montserrat",sans-serif;font-weight:700;font-size:11.5px;color:var(--orange);text-decoration:underline}

.follow{left:836px;top:1098px;width:280px;height:105px;border-top:7px solid #dcdcdc;border-bottom:7px solid #dcdcdc}
.follow .widget-title{left:12px;top:10px}
.follow-list{left:12px;top:36px;width:254px;display:flex;justify-content:space-between}
.follow-item{display:flex;flex-direction:column;align-items:center;width:46px}
.follow-item i{display:block;width:32px;height:32px}
.follow-item span{margin-top:3px;font-family:"Montserrat",sans-serif;font-weight:600;font-size:9px;color:var(--ink);white-space:nowrap}

.archives{left:836px;top:1238px;width:280px;height:219px}
.archives .widget-title{left:13px;top:10px;color:var(--navy)}
.archive-list{left:13px;top:36px;width:252px;list-style:none}
.archive-list li{font-family:"Montserrat",sans-serif;font-weight:600;font-size:12px;color:var(--ink);height:25.4px;line-height:25px;border-bottom:1px solid var(--line)}
.archive-list li:last-child{border-bottom:0}

.tags{left:836px;top:1490px;width:280px;height:172px}
.tags .widget-title{left:13px;top:12px;color:var(--navy)}
.tag-cloud{left:13px;top:43px;width:262px;display:flex;flex-wrap:wrap;gap:5px 4px}
.tag-cloud span{display:block;height:31px;line-height:31px;padding:0 15px;background:var(--orange);color:var(--white);font-family:"Montserrat",sans-serif;font-weight:700;font-size:13.5px}

.promo{left:836px;top:1713px;width:280px;height:247px;background:linear-gradient(160deg,#6b4a3c 0%,#3a2b2a 45%,#15110f 100%)}

/* about */
.about{left:0;top:2000px;width:1200px;height:336px;background:var(--orange)}
.about-photo{left:146px;top:47px;width:253px;height:254px;border:4px solid #d9d9d9;background:linear-gradient(135deg,#d9dde3 0%,#a9b4c0 60%,#7c8a99 100%)}
.about-title{left:435px;top:52px;font-family:"Montserrat",sans-serif;font-weight:700;font-size:23px;color:var(--white)}
.about-text{left:435px;top:96px;width:594px;font-size:13px;line-height:20.3px;color:var(--white)}
.about-more{left:445px;top:270px;font-family:"Montserrat",sans-serif;font-weight:700;font-size:15px;color:var(--white)}

.site-footer{left:0;top:2336px;width:1200px;height:45px;background:var(--footer);text-align:center;line-height:45px;font-family:"Montserrat",sans-serif;font-weight:600;font-size:11px;color:var(--white)}
</style>
</head>
<body>

<svg width="0" height="0" style="position:absolute" aria-hidden="true">
  <defs>
    <symbol id="i-cal" viewBox="0 0 14 14"><rect x="1" y="2.5" width="12" height="10.5" rx="1"/><rect x="3" y="0.5" width="1.8" height="3.5" rx=".5"/><rect x="9.2" y="0.5" width="1.8" height="3.5" rx=".5"/><rect x="2.5" y="5.5" width="9" height="6" fill="#fff"/></symbol>
    <symbol id="i-chat" viewBox="0 0 14 14"><path d="M7 1.5c3.6 0 6.5 2.2 6.5 5s-2.9 5-6.5 5c-.7 0-1.3-.1-1.9-.2L1.5 13l1.1-2.9C1.3 9.2.5 7.9.5 6.5c0-2.8 2.9-5 6.5-5z"/></symbol>
    <symbol id="i-share" viewBox="0 0 14 14"><path d="M8 2l5.5 4.5L8 11V8.3C4.6 8.3 2.4 9.4.5 12c.6-4 2.9-6.9 7.5-7.3z"/></symbol>
    <symbol id="i-clock" viewBox="0 0 14 14"><path d="M7 .5a6.5 6.5 0 1 1 0 13 6.5 6.5 0 0 1 0-13zm0 1.6a4.9 4.9 0 1 0 0 9.8 4.9 4.9 0 0 0 0-9.8zM6.2 3.5h1.5v3.3l2.4 1.4-.8 1.3-3.1-1.9z"/></symbol>
  </defs>
</svg>

<header class="abs site-header">
  <div class="abs brand">Folio K</div>
  <nav class="abs nav">
    <a class="active" href="#">About Me</a>
    <a href="#">Recent Blog</a>
    <a href="#">Reader Comments</a>
    <a href="#">Contact Us</a>
  </nav>
  <div class="abs social-top"><span>Facet</span><span>Chirpa</span><span>Feed</span><span>Linkr</span></div>
</header>

<section class="abs hero" role="img" aria-label="Photo of a person with raised arms on a cliff edge at sunset"></section>
<p class="abs hero-text">Lorem ipsum dolor sit amet, consectetuer adipiscing elit, sed nonummy nibh euismod</p>
<div class="abs hero-dashes"><span></span><span></span><span></span></div>

<main>
  <article class="abs card featured">
    <div class="abs featured-photo" role="img" aria-label="Photo of a woman with open arms against a golden sunset sky"></div>
    <div class="abs meta featured-meta">
      <svg><use href="#i-clock"/></svg><span class="date">MAY 18, 2015 &nbsp;|&nbsp; BY</span><b>Lorem Ipsum</b>
      <span class="gap" style="margin-left:62px"></span><svg><use href="#i-cal"/></svg>June 18, 2016
      <span class="gap"></span><svg><use href="#i-chat"/></svg>No Comments
      <span class="gap" style="margin-left:44px"></span>Share&nbsp;<svg><use href="#i-share"/></svg>
    </div>
    <h2 class="abs featured-title">Lorem Ipsum Dolor Sit Amet</h2>
    <p class="abs featured-text">Lorem ipsum dolor sit amet, consectetuer adipiscing elit, sed diam nonummy nibh euismod tincidunt ut laoreet dolore magna aliquam erat volutpat.</p>
    <a class="abs btn featured-btn" href="#">READ MORE</a>
  </article>

  <div class="abs rule" style="top:1030px"></div>
  <div class="abs rule" style="top:1266px"></div>
  <div class="abs rule" style="top:1503px"></div>
  <div class="abs rule" style="top:1741px"></div>

  <article class="abs card post" style="left:84px;top:1049px">
    <h3 class="abs post-title">Lorem ipsum dolor sit amet consecit</h3>
    <div class="abs meta post-meta"><svg><use href="#i-cal"/></svg>June 18, 2016<span class="gap"></span><svg><use href="#i-chat"/></svg>No Comments<span class="gap"></span>Share&nbsp;<svg><use href="#i-share"/></svg></div>
    <div class="abs post-thumb" role="img" aria-label="Photo of a couple embracing" style="background:linear-gradient(135deg,#8a5a48,#c98f76)"></div>
    <p class="abs post-text">Lorem ipsum dolor sit amet, consecit adipiscing elit, sed do eiusmod tempor incidimen labore n dolorme laboris ni ut ullamc...... <a href="#">Read More</a></p>
  </article>
  <article class="abs card post" style="left:446px;top:1049px">
    <h3 class="abs post-title">Lorem ipsum dolor sit amet consecit</h3>
    <div class="abs meta post-meta"><svg><use href="#i-cal"/></svg>June 18, 2016<span class="gap"></span><svg><use href="#i-chat"/></svg>No Comments<span class="gap"></span>Share&nbsp;<svg><use href="#i-share"/></svg></div>
    <div class="abs post-thumb" role="img" aria-label="Photo of a smiling woman outdoors" style="background:linear-gradient(135deg,#c9d39a,#b5655a)"></div>
    <p class="abs post-text">Lorem ipsum dolor sit amet, consecit adipiscing elit, sed do eiusmod tempor incidimen labore n dolorme laboris ni ut ullamc...... <a href="#">Read More</a></p>
  </article>

  <article class="abs card post" style="left:84px;top:1286px">
    <h3 class="abs post-title">Lorem ipsum dolor sit amet consecit</h3>
    <div class="abs meta post-meta"><svg><use href="#i-cal"/></svg>June 18, 2016<span class="gap"></span><svg><use href="#i-chat"/></svg>No Comments<span class="gap"></span>Share&nbsp;<svg><use href="#i-share"/></svg></div>
    <div class="abs post-thumb" role="img" aria-label="Photo of a woman in a yellow flower field" style="background:linear-gradient(180deg,#f0b82b,#c7a014)"></div>
    <p class="abs post-text">Lorem ipsum dolor sit amet, consecit adipiscing elit, sed do eiusmod tempor incidimen labore n dolorme laboris ni ut ullamc...... <a href="#">Read More</a></p>
  </article>
  <article class="abs card post" style="left:446px;top:1286px">
    <h3 class="abs post-title">Lorem ipsum dolor sit amet consecit</h3>
    <div class="abs meta post-meta"><svg><use href="#i-cal"/></svg>June 18, 2016<span class="gap"></span><svg><use href="#i-chat"/></svg>No Comments<span class="gap"></span>Share&nbsp;<svg><use href="#i-share"/></svg></div>
    <div class="abs post-thumb" role="img" aria-label="Photo of a person jumping on a green meadow" style="background:linear-gradient(180deg,#7ea7d8 0%,#a9c4e4 50%,#5d9a3a 100%)"></div>
    <p class="abs post-text">Lorem ipsum dolor sit amet, consecit adipiscing elit, sed do eiusmod tempor incidimen labore n dolorme laboris ni ut ullamc...... <a href="#">Read More</a></p>
  </article>

  <article class="abs card post" style="left:84px;top:1522px">
    <h3 class="abs post-title">Lorem ipsum dolor sit amet consecit</h3>
    <div class="abs meta post-meta"><svg><use href="#i-cal"/></svg>June 18, 2016<span class="gap"></span><svg><use href="#i-chat"/></svg>No Comments<span class="gap"></span>Share&nbsp;<svg><use href="#i-share"/></svg></div>
    <div class="abs post-thumb" role="img" aria-label="Photo of a silhouette leaping against an orange sunset" style="background:linear-gradient(180deg,#f28a12,#5a2a08)"></div>
    <p class="abs post-text">Lorem ipsum dolor sit amet, consecit adipiscing elit, sed do eiusmod tempor incidimen labore n dolorme laboris ni ut ullamc...... <a href="#">Read More</a></p>
  </article>
  <article class="abs card post" style="left:446px;top:1522px">
    <h3 class="abs post-title">Lorem ipsum dolor sit amet consecit</h3>
    <div class="abs meta post-meta"><svg><use href="#i-cal"/></svg>June 18, 2016<span class="gap"></span><svg><use href="#i-chat"/></svg>No Comments<span class="gap"></span>Share&nbsp;<svg><use href="#i-share"/></svg></div>
    <div class="abs post-thumb" role="img" aria-label="Photo of a woman in a sunlit garden" style="background:linear-gradient(135deg,#e8f0c8,#6f9a44)"></div>
    <p class="abs post-text">Lorem ipsum dolor sit amet, consecit adipiscing elit, sed do eiusmod tempor incidimen labore n dolorme laboris ni ut ullamc...... <a href="#">Read More</a></p>
  </article>

  <article class="abs card post" style="left:84px;top:1759px">
    <h3 class="abs post-title">Lorem ipsum dolor sit amet consecit</h3>
    <div class="abs meta post-meta"><svg><use href="#i-cal"/></svg>June 18, 2016<span class="gap"></span><svg><use href="#i-chat"/></svg>No Comments<span class="gap"></span>Share&nbsp;<svg><use href="#i-share"/></svg></div>
    <div class="abs post-thumb" role="img" aria-label="Photo of a man with raised arms in a sunny field" style="background:linear-gradient(180deg,#f6e27a,#9aa62c)"></div>
    <p class="abs post-text">Lorem ipsum dolor sit amet, consecit adipiscing elit, sed do eiusmod tempor incidimen labore n dolorme laboris ni ut ullamc...... <a href="#">Read More</a></p>
  </article>
  <article class="abs card post" style="left:446px;top:1759px">
    <h3 class="abs post-title">Lorem ipsum dolor sit amet consecit</h3>
    <div class="abs meta post-meta"><svg><use href="#i-cal"/></svg>June 18, 2016<span class="gap"></span><svg><use href="#i-chat"/></svg>No Comments<span class="gap"></span>Share&nbsp;<svg><use href="#i-share"/></svg></div>
    <div class="abs post-thumb" role="img" aria-label="Photo of a laughing woman close up" style="background:linear-gradient(135deg,#e9a26a,#b5533a)"></div>
    <p class="abs post-text">Lorem ipsum dolor sit amet, consecit adipiscing elit, sed do eiusmod tempor incidimen labore n dolorme laboris ni ut ullamc...... <a href="#">Read More</a></p>
  </article>
</main>

<aside>
  <section class="abs widget newsletter">
    <h4 class="abs widget-title">Newsletter Sign Up</h4>
    <div class="abs email">Enter Your Email Address</div>
    <a class="abs btn subscribe" href="#">SUBSCRIBE</a>
  </section>

  <section class="abs widget tabs">
    <div class="abs tab-bar"><span class="on">Page Views</span><span>Social Shares#</span><span class="last">Comments</span></div>
    <div class="abs tab-item" style="top:49px">
      <div class="abs tab-thumb" role="img" aria-label="Photo of a woman on a green lawn" style="background:linear-gradient(135deg,#b9d38a,#5e8a34)"></div>
      <p class="abs tab-text">Lorem ipsum dolor sit ame consectetuer adipiscing Dolor sit almet</p>
    </div>
    <div class="abs tab-item" style="top:131px">
      <div class="abs tab-thumb" role="img" aria-label="Photo of a smiling woman in a meadow" style="background:linear-gradient(135deg,#f3f0c0,#a9bf5a)"></div>
      <p class="abs tab-text">Lorem ipsum dolor sit ame consectetuer adipiscing Dolor sit almet</p>
    </div>
    <div class="abs tab-item" style="top:213px">
      <div class="abs tab-thumb" role="img" aria-label="Portrait photo of a smiling man" style="background:linear-gradient(135deg,#e4e6ea,#9ea7b2)"></div>
      <p class="abs tab-text">Lorem ipsum dolor sit ame consectetuer adipiscing Dolor sit almet</p>
    </div>
    <a class="abs view-all" href="#">View All &gt;&gt;</a>
  </section>

  <section class="abs widget follow">
    <h4 class="abs widget-title">Follow Us</h4>
    <div class="abs follow-list">
      <a class="follow-item" href="#"><i style="background:var(--net-blue)"></i><span>Facet</span></a>
      <a class="follow-item" href="#"><i style="background:var(--net-red)"></i><span>Circlo</span></a>
      <a class="follow-item" href="#"><i style="background:var(--net-sky)"></i><span>Chirpa</span></a>
      <a class="follow-item" href="#"><i style="background:var(--net-crimson)"></i><span>Reelo</span></a>
      <a class="follow-item" href="#"><i style="background:var(--net-deep)"></i><span>Linkr</span></a>
    </div>
  </section>

  <section class="abs widget archives">
    <h4 class="abs widget-title">Archives</h4>
    <ul class="abs archive-list">
      <li>July 2016</li><li>June 2016</li><li>May 2016</li><li>April 2016</li><li>March 2016</li><li>February 2016</li><li>January 2016</li>
    </ul>
  </section>

  <section class="abs widget tags">
    <h4 class="abs widget-title">Popular Tags</h4>
    <div class="abs tag-cloud">
      <span>SIT</span><span>DOLOR</span><span>ALMETSIT</span><span>DOLOR</span><span>ELIT</span><span>SIT</span><span>ELIT</span><span>ALMETS</span>
    </div>
  </section>

  <div class="abs promo" role="img" aria-label="Advertisement photo of an off-road truck at dusk"></div>
</aside>

<section class="abs about">
  <div class="abs about-photo" role="img" aria-label="Portrait photo of the blog author"></div>
  <h2 class="abs about-title">About Me</h2>
  <p class="abs about-text">Lorem ipsum dolor sit amet, consectetuer adipiscing elit, sed diam nonummy nibh euismod alme tincidunt ut laoreet dolore magna aliquam erat volutpat. Ut wisi enim ad minim veniam, quis dol nostrud exerci tation ullamcorper suscipit lobortis nisl ut aliquip ex ea commodo consequat list Duis autem vel eum iriure dolor in hendrerit in vulputate velit esse molestie consequat, vel alm illum dolore eu feugiat nulla facilisis at vero eros et accumsan et iusto odio dignissim qui blandit illum dolore eu feugiat nulla facilisis at vero eros et accumsan et iusto odio dignissim qui blandit praesent luptatum zzril delenit augue duis dolore te feugait nulla facilisi.</p>
  <a class="abs about-more" href="#">Read More</a>
</section>

<footer class="abs site-footer">Copyright © 2016 Folio K. All Rights Reserved.</footer>

</body>
</html>
```